A front Sign for The Kelverton Orthopaedic Centre

A sign for the front of our consulting rooms. Utilising logo winner of competition 3757477. Business card and letterhead competition 3793183. Specialist Orthopaedic surgeons. includes a phone number.

```html
<!DOCTYPE html>
<html lang="en">
<head>
<meta charset="utf-8">
<title>The Kelverton Orthopaedic Centre – Front Sign</title>
<link rel="stylesheet" href="https://fonts.googleapis.com/css2?family=Montserrat:wght@500;600;700;800&display=swap">
<style>
  :root {
    --navy: #0a3450;
    --sky: #33aef5;
    --sky-deep: #2a8fd6;
    --white: #ffffff;
    --backdrop: #d9dcdf;
  }
  html, body {
    margin: 0;
    padding: 0;
    width: 1200px;
    height: 540px;
    overflow: hidden;
    background: var(--backdrop);
  }
  .sign {
    position: absolute;
    left: 40px;
    top: 158px;
    width: 1120px;
    height: 224px;
    display: block;
    font-family: "Montserrat", sans-serif;
  }
  .practice-name { fill: var(--navy); font-weight: 500; font-size: 28px; }
  .web-pill { fill: var(--sky); }
  .web-address { fill: var(--white); font-weight: 600; font-size: 15px; }
  .headline { fill: var(--sky); font-weight: 800; font-size: 56px; }
  .subline-box { fill: var(--sky); }
  .subline { fill: var(--white); font-weight: 700; font-size: 25px; }
  .wave-band { fill: var(--sky); }
  .wave-base { fill: var(--navy); stroke: var(--white); stroke-width: 3; }
  .phone-icon { fill: none; stroke: var(--white); stroke-width: 2.2; }
  .phone-handset { fill: var(--white); }
  .phone-number { fill: var(--white); font-weight: 700; font-size: 34px; }
</style>
</head>
<body>
<svg class="sign" viewBox="0 0 1120 224" xmlns="http://www.w3.org/2000/svg" aria-label="The Kelverton Orthopaedic Centre front sign">
  <defs>
    <linearGradient id="pillFill" x1="0" y1="0" x2="1" y2="0">
      <stop offset="0" stop-color="var(--sky-deep)"/>
      <stop offset="1" stop-color="var(--sky)"/>
    </linearGradient>
  </defs>

  <rect class="sign-face" x="0" y="0" width="1120" height="224" fill="var(--white)"/>

  <!-- wave bands -->
  <path class="wave-band" d="M0,128 C200,195 500,200 780,134 C900,112 1000,140 1050,164 L1120,224 L0,224 Z"/>
  <path class="wave-base" d="M0,157 C250,215 520,200 800,146 C920,124 1020,158 1120,193 L1120,240 L-10,240 Z"/>

  <!-- practice name -->
  <text class="practice-name" x="48" y="96" textLength="518" lengthAdjust="spacingAndGlyphs">The Kelverton Orthopaedic Centre</text>

  <!-- web address -->
  <rect class="web-pill" x="130" y="122" width="310" height="32" rx="16" fill="url(#pillFill)"/>
  <text class="web-address" x="285" y="143" text-anchor="middle">www.KelvertonOrtho.com</text>

  <!-- headline block -->
  <text class="headline" x="636" y="78" textLength="416" lengthAdjust="spacing">SPECIALIST</text>
  <rect class="subline-box" x="636" y="86" width="415" height="36"/>
  <text class="subline" x="843" y="114" text-anchor="middle" textLength="370" lengthAdjust="spacingAndGlyphs">ORTHOPAEDIC SURGEONS</text>

  <!-- phone -->
  <circle class="phone-icon" cx="712" cy="188" r="16"/>
  <path class="phone-handset" d="M705,179 c1.5,-1.5 3,-1 3.8,0.4 l1.6,3 c0.6,1.2 0.2,2.2 -0.8,2.9 l-1,0.7 c0.8,2.6 2.8,4.9 5.4,6 l0.8,-1 c0.8,-1 1.9,-1.2 3,-0.5 l2.8,1.8 c1.3,0.9 1.5,2.3 0.2,3.6 l-1.3,1.3 c-1.8,1.8 -5,1.2 -8.4,-1.6 c-3.4,-2.8 -6,-6.4 -7.2,-9.8 c-0.8,-2.4 -0.6,-4.6 0.8,-6 Z"/>
  <text class="phone-number" x="745" y="201">(123) 555-0148</text>
</svg>
</body>
</html>
```